We are the world's leading center for transgender surgery and have multiple locations.

We want a unique and dynamic business card that wows potential patients and referral sources (physicians, previous patients, etc). We are open to inventive designs, card shape, additional design on the back of the card, etc.

We are a surgical practice in a competitive environment and want to stand out as the leader in transgender surgery. We have multiple surgeons with unique talents who are impeccably trained with extensive experience. We are dedicated to our patients and their needs. We want the card to stand out and impress them. We want it to be suitable to all of the surgeons as well as our staff.

Our practice started as a small practice in San Francisco, CA and now has an additional location in Austin Texas (as well as another city to be announced later). Our practice has plastic surgeons, reconstructive urologists, general surgeons and gynecologists.

We continue to boast some of the lowest published phalloplasty complication rates in the world and our San Francisco microsurgeons that we have been working with for more than a year and a half have 0 microvascular take backs and 0 flap failures. Between our two centers in San Francisco, California and Austin, Texas, we perform 5-6 phalloplasties per week, making us one of the largest volume centers in the world.

Target Market(s)

Potential Transgender patients (all genders) and referring physicians

Industry/Entity Type

Surgeon

Contact Information for Business Card

Here is an example of one of our physicians:

Daniel R. Ostrow, MD
Reconstructive Urology for the Transgender Community
Diplomate, National Council of Renal Medicine with subspecialty certification in FPS and Reconstructive Surgery

318 Lady Harriet Moore Ave
Suite 7
Harlow Bay, CA 94817

phone 415-738-1942
fax 415-582-1947

Font styles to use
Sans Serif

Requirements
Must have
• Must have a unique look, but tasteful.
Nice to have
• ?
Should not have
• ?

```html
<!DOCTYPE html>
<html lang="en">
<head>
<meta charset="utf-8">
<title>Alder Clinic – Business Card</title>
<link rel="stylesheet" href="https://fonts.googleapis.com/css2?family=Saira:wght@600&family=Questrial&display=swap">
<style>
  :root {
    --magenta: #9c0a63;
    --navy: #0e2c73;
    --paper: #ffffff;
    --backdrop: #2b2b2d;
  }
  * { margin: 0; padding: 0; box-sizing: border-box; }
  html, body { width: 1200px; height: 801px; overflow: hidden; }
  body {
    background: var(--backdrop);
    position: relative;
    font-family: "Questrial", Arial, sans-serif;
  }
  .card {
    position: absolute;
    width: 560px;
    height: 320px;
    background: var(--paper);
    overflow: hidden;
    box-shadow: 0 10px 24px rgba(0,0,0,.45);
  }
  .card-front { left: 540px; top: 48px; }
  .card-back  { left: 130px; top: 410px; }

  .brand {
    font-family: "Saira", Arial, sans-serif;
    font-weight: 600;
    color: var(--magenta);
    line-height: 1;
  }
  .card-front .brand {
    position: absolute; left: 30px; top: 30px;
    font-size: 30px;
  }
  .physician {
    position: absolute; left: 30px; top: 96px; width: 290px;
  }
  .physician-name {
    font-family: "Saira", Arial, sans-serif;
    font-weight: 600;
    font-size: 18px;
    color: var(--magenta);
    margin-bottom: 6px;
  }
  .physician-title {
    font-size: 12.5px;
    line-height: 1.3;
    color: var(--navy);
  }
  .contact-band {
    position: absolute; left: 0; right: 0; bottom: 0; height: 118px;
    background: var(--magenta);
  }
  .contact {
    position: absolute; left: 30px; bottom: 20px;
    color: var(--paper);
    font-size: 15px;
    font-style: normal;
    line-height: 1.35;
  }
  .contact-line { display: flex; align-items: center; gap: 8px; }
  .contact-line svg { width: 13px; height: 13px; fill: var(--paper); }

  .card-back .back-logo {
    position: absolute; left: 0; right: 0; top: 50%;
    transform: translateY(-50%);
    display: flex; align-items: center; justify-content: center; gap: 18px;
  }
  .back-logo .mark-dot {
    width: 70px; height: 70px; border-radius: 50%;
    background: var(--navy);
  }
  .back-logo .brand { font-size: 44px; }
</style>
</head>
<body>

  <section class="card card-front" aria-label="Business card, front">
    <div class="brand">Alder Clinic</div>

    <div class="physician">
      <h1 class="physician-name">DANIEL R. OSTROW, MD</h1>
      <p class="physician-title">Reconstructive Urology for the Transgender Community Diplomate, National Council of Renal Medicine with subspecialty certification in FPS and Reconstructive Surgery</p>
    </div>

    <div class="contact-band"></div>

    <address class="contact">
      <div>318 Lady Harriet Moore Ave</div>
      <div>Suite 7 Harlow Bay, CA 94817</div>
      <div class="contact-line">
        <svg viewBox="0 0 24 24" aria-label="phone"><path d="M6.6 10.8a15 15 0 0 0 6.6 6.6l2.2-2.2a1 1 0 0 1 1-.25 11.4 11.4 0 0 0 3.6.57 1 1 0 0 1 1 1V20a1 1 0 0 1-1 1A17 17 0 0 1 3 4a1 1 0 0 1 1-1h3.5a1 1 0 0 1 1 1c0 1.25.2 2.45.57 3.57a1 1 0 0 1-.25 1z"/></svg>
        <span>415-738-1942</span>
      </div>
      <div class="contact-line">
        <svg viewBox="0 0 24 24" aria-label="fax"><path d="M7 3h10v5H7zM4 9h16a2 2 0 0 1 2 2v6h-4v4H6v-4H2v-6a2 2 0 0 1 2-2zm4 7v3h8v-3z"/></svg>
        <span>415-582-1947</span>
      </div>
    </address>
  </section>

  <section class="card card-back" aria-label="Business card, back">
    <div class="back-logo">
      <span class="mark-dot" aria-hidden="true"></span>
      <span class="brand">Alder Clinic</span>
    </div>
  </section>

</body>
</html>
```